Design 6.5 x 9 Postcard for Business

You will need to design a 6.5" x 9" postcard for our insulation business, Vornel Thermal, LLC based on design requirements. We will be using Postwisp and have attached template for guide. Must include phone number, web address, company logo, tidal keep partner logo and marketing call to action. Specificallyl marketing 75-100% off insulation & weatheriation services with FREE Home Energy Assessment. Absolutely no cost. I have given examples of other companies on attachment as well for inspiration. I will also need to ensure that somewhere clear is "Our company just insulated a home on your mail route and we'd like to offer you a FREE assessment!"

Here are competitior websites for inspiration.

https://www.quellohome.example/?gclid=EAIaIQobChMI3PqbgNaL6gIVgZOzCh3-AQG1EAAYASAAEgKziPD_BwE

https://www.brambleloftheat.example/

```html
<!DOCTYPE html>
<html lang="en">
<head>
<meta charset="utf-8">
<title>Vornel Thermal Postcard</title>
<link rel="stylesheet" href="https://fonts.googleapis.com/css2?family=Barlow:ital,wght@0,600;0,700;0,800;1,800&family=Barlow+Condensed:wght@500;700&display=swap">
<style>
  :root {
    --page: #e6e7e9;
    --navy: #174a86;
    --blue: #1f6fb8;
    --periwinkle: #8ea2cf;
    --white: #ffffff;
    --photo-a: #6f7f6a;
    --photo-b: #8a8f94;
    --photo-c: #7ea3cf;
    --badge: #222222;
  }
  * { box-sizing: border-box; margin: 0; padding: 0; }
  html, body { width: 1200px; height: 533px; overflow: hidden; }
  body { background: var(--page); position: relative; font-family: "Barlow", sans-serif; }

  .postcard {
    position: absolute; top: 84px; width: 505px; height: 364px;
    overflow: hidden; box-shadow: 3px 4px 8px rgba(0,0,0,.35);
  }
  .postcard--front { left: 84px; }
  .postcard--back { left: 611px; }
  .postcard__bg { position: absolute; inset: 0; width: 100%; height: 100%; }

  .brand { position: absolute; display: flex; align-items: center; gap: 8px; }
  .brand__square { width: 14px; height: 14px; }
  .brand__name { font-family: "Barlow", sans-serif; font-weight: 700; font-size: 30px; letter-spacing: .5px; line-height: 1; }
  .postcard--front .brand { left: 30px; top: 55px; }
  .postcard--front .brand__square { background: var(--navy); }
  .postcard--front .brand__name { color: var(--navy); }
  .postcard--back .brand { left: 33px; top: 42px; }
  .postcard--back .brand__square { background: var(--white); }
  .postcard--back .brand__name { color: var(--white); }

  .headline__top {
    position: absolute; right: 27px; top: 40px;
    font-weight: 800; font-size: 34px; color: var(--white); line-height: 1;
  }
  .headline__tag { position: absolute; left: 259px; top: 75px; width: 229px; height: 39px; }
  .headline__tag-text {
    position: absolute; right: 27px; top: 77px;
    font-weight: 800; font-style: italic; font-size: 33px; color: var(--navy); line-height: 1;
  }

  .service { position: absolute; top: 135px; width: 152px; text-align: center; }
  .service__photo { height: 115px; border: 1px solid rgba(255,255,255,.8); }
  .service__label {
    margin-top: 12px; font-family: "Barlow Condensed", sans-serif; font-weight: 700;
    font-size: 16.5px; line-height: 19px; color: var(--white); letter-spacing: .2px;
  }
  .service--assessments { left: 8px; }
  .service--assessments .service__photo { background: linear-gradient(135deg, var(--photo-a), #b9a58f); }
  .service--sealing { left: 168px; }
  .service--sealing .service__photo { background: linear-gradient(135deg, var(--photo-b), #c9c2b8); }
  .service--hvac { left: 328px; }
  .service--hvac .service__photo { background: linear-gradient(135deg, #cfd4d8, var(--photo-c)); }

  .contact-bar {
    position: absolute; left: 30px; top: 332px;
    font-weight: 800; font-size: 18px; color: var(--navy); line-height: 1;
  }
  .partner-badge {
    position: absolute; left: 392px; top: 308px; width: 46px; height: 46px;
    border-radius: 50%; background: var(--badge);
  }

  .back__copy { position: absolute; left: 33px; top: 100px; }
  .back__para {
    font-weight: 700; font-size: 11px; line-height: 13.3px; color: var(--white); margin-bottom: 13px;
  }
  .back__para--wide { width: 330px; }
  .back__para--mid { width: 280px; }
  .back__para--narrow { width: 215px; }
  .back__phone {
    position: absolute; left: 33px; top: 278px;
    font-weight: 800; font-size: 21px; color: var(--white); line-height: 1;
  }
  .back__web {
    position: absolute; left: 33px; top: 305px;
    font-weight: 800; font-size: 20px; color: var(--white); line-height: 1;
  }
</style>
</head>
<body>

<section class="postcard postcard--front">
  <svg class="postcard__bg" viewBox="0 0 505 364" preserveAspectRatio="none" aria-hidden="true">
    <defs>
      <linearGradient id="front-base" x1="0" y1="0" x2="1" y2="0.3">
        <stop offset="0" stop-color="#8ea2cf"/>
        <stop offset="0.45" stop-color="#3f7cc0"/>
        <stop offset="1" stop-color="#1f68b0"/>
      </linearGradient>
    </defs>
    <rect width="505" height="364" fill="url(#front-base)"/>
    <polygon points="0,0 150,0 0,150" fill="#a3b3da" opacity=".55"/>
    <polygon points="240,0 300,0 0,300 0,240" fill="#ffffff" opacity=".08"/>
    <polygon points="330,0 505,0 505,60 140,364 0,364" fill="#1a62ad" opacity=".35"/>
    <polygon points="505,260 505,300 440,364 400,364" fill="#a3b3da" opacity=".5"/>
    <polygon points="0,220 80,364 0,364" fill="#ffffff" opacity=".06"/>
    <polygon points="0,320 300,320 330,303 505,303 505,364 0,364" fill="#ffffff"/>
  </svg>

  <div class="brand">
    <span class="brand__square"></span>
    <span class="brand__name">Vornel Thermal</span>
  </div>

  <div class="headline__top">ENERGY</div>
  <svg class="headline__tag" viewBox="0 0 229 39" aria-hidden="true">
    <polygon points="30,0 229,0 229,39 0,39" fill="#ffffff"/>
  </svg>
  <div class="headline__tag-text">INSULATION</div>

  <div class="service service--assessments">
    <div class="service__photo" role="img" aria-label="Technician reviewing an energy report with a homeowner indoors"></div>
    <div class="service__label">HOME ENERGY<br>ASSESSMENTS</div>
  </div>
  <div class="service service--sealing">
    <div class="service__photo" role="img" aria-label="Worker sealing gaps in a house's exterior siding"></div>
    <div class="service__label">INSULATION &amp;<br>AIR SEALING</div>
  </div>
  <div class="service service--hvac">
    <div class="service__photo" role="img" aria-label="Crew on a ladder servicing a house exterior under blue sky"></div>
    <div class="service__label">HEATING &amp;<br>COOLING</div>
  </div>

  <div class="contact-bar">0123 456 789 | www.vornel.example</div>
  <div class="partner-badge" role="img" aria-label="Partner program badge"></div>
</section>

<section class="postcard postcard--back">
  <svg class="postcard__bg" viewBox="0 0 505 364" preserveAspectRatio="none" aria-hidden="true">
    <defs>
      <linearGradient id="back-base" x1="0" y1="0" x2="1" y2="0.3">
        <stop offset="0" stop-color="#8ea2cf"/>
        <stop offset="0.45" stop-color="#3f7cc0"/>
        <stop offset="1" stop-color="#1f68b0"/>
      </linearGradient>
    </defs>
    <rect width="505" height="364" fill="url(#back-base)"/>
    <polygon points="0,0 150,0 0,150" fill="#a3b3da" opacity=".55"/>
    <polygon points="240,0 300,0 0,300 0,240" fill="#ffffff" opacity=".08"/>
    <polygon points="330,0 505,0 505,20 140,364 0,364" fill="#1a62ad" opacity=".35"/>
    <polygon points="0,260 60,364 0,364" fill="#ffffff" opacity=".06"/>
    <polygon points="505,21 505,364 161,364" fill="#ffffff"/>
  </svg>

  <div class="brand">
    <span class="brand__square"></span>
    <span class="brand__name">Vornel Thermal</span>
  </div>

  <div class="back__copy">
    <p class="back__para back__para--wide">Our company just insulated a home on your mail route and we'd like to offer you a FREE assessment!</p>
    <p class="back__para back__para--mid">Save 75-100% off insulation &amp; weatherization services when you book your FREE Home Energy Assessment.</p>
    <p class="back__para back__para--narrow">Absolutely no cost to you. Call us today to schedule your visit.</p>
  </div>

  <div class="back__phone">Ph: 0123 456 789</div>
  <div class="back__web">vornel.example</div>
</section>

</body>
</html>
```